Customizable Form Generation Website

This will be a place for users to quickly generate numerous forms from a categorized list. As the forms are templates with field variables, the site must be able to substitute ‘real data’ for template variable data. This tool will allow for quick custom forms on-demand.

The landing page is attached. We need the User Experience and User Interface solved for us.

EXAMPLE:
——————————————————————-
Dear {{PatientFirstName}},

Please come back for an examination on {{SelectedDate}} with Doctor {{SelectedProvider}}.

Sincerely,

{{SelectedAuthor}}
——————————————————————-

Coming to the Forms Landing Page, the user will see the forms available to select. The user will then click to select a form.

At some point, the user must resolve the variables in the form. For instance, there are the following variables in the above example: PatientFirstName, SelectedDate, SelectedProvider, and SelectedAuthor. We must give the user a chance to select the values for these variables. Using a dropdown combobox will probably work for most. Getting a date selector will be required if the variable happens to contain the string 'date'.

Is it best to preselect common variables before opening the form, or is it best to dynamically scan the template, then give the user the option to give values to each variable found?

The design must include a way for users to upload additional forms. Forms will most probably be PDF, .DOC, .TXT files. This allows users to develop simple or fancy forms of their choosing., then simply drop them into the site for future use.

The design must include a way for users to create new forms. The form creation tool must present to the user the list of predefined variables like {{PatientLastName}} for easy insertion into the form writer. Anytime "{{}}" are used, developers will recognize that as a variable that needs to be resolved.

The forms will be separated into categories as follows:

OFFICE:
- Letterhead
- Sign-In Sheet
- Fax Cover Sheet
SCHEDULER:
- Appointment Reminder
- Missed Appointment Policy
PATIENT:
- Intake Form
- Patient Discharge
- Return to Work or School
- Excuse Slip
- Consent to Treat a Minor
- Verify Non-Pregnancy
RELEASE:
- Health Information Release Form
- X-Ray Release Form
CERTIFICATES:
- Certificate of Care
- Disability Certificate
INSURANCE:
- Authorization to Bill Insurance
- Assignment Authorization
OTHER:
- Free Massage
- Free Vitamins

The design must include a way to add/customize categories. Categories are for organizing the forms logically.

We welcome ANY questions to help understand the requirements.

Good luck!

Industry/Entity Type

Healthcare

Number of Pages Required

3 page

Requirements
Must have
• Must Follow VELLUM PATTERN standards
Nice to have
• Great User Experience. Simple, Fast, Clever.
Should not have
• nothing to add here

```html
<!DOCTYPE html>
<html lang="en">
<head>
<meta charset="utf-8">
<title>Forms Dashboard</title>
<link href="https://fonts.googleapis.com/css2?family=Lato:ital,wght@0,400;0,700;1,700&display=swap" rel="stylesheet">
<style>
:root{
  --stage:#3a3a3a;
  --sidebar:#07648f;
  --orange:#f99d1c;
  --ink:#0b5d86;
  --text:#3c3c3c;
  --muted:#555b60;
  --page-a:#eef5f9;
  --page-b:#e2eef5;
  --white:#ffffff;
  --field:#f7f8fa;
}
*{box-sizing:border-box;margin:0;padding:0}
html,body{width:1200px;height:529px;overflow:hidden}
body{background:var(--stage);font-family:'Lato',sans-serif;position:relative}
.screen{position:absolute;top:48px;width:550px;height:433px;background:linear-gradient(160deg,var(--page-a),var(--page-b));overflow:hidden}
.screen--session{left:35px}
.screen--forms{left:614px}
.sidebar{position:absolute;left:0;top:0;width:81.5px;height:100%;background:var(--sidebar)}
.menu-toggle{position:absolute;left:12px;top:12px}
.nav{list-style:none;position:absolute;top:0;left:0;width:100%}
.nav-item{position:absolute;left:0;width:100%;height:14px;display:flex;align-items:center;color:var(--white);font-size:6.6px;letter-spacing:.1px}
.nav-item svg{position:absolute;left:12px;width:8px;height:8px}
.nav-item span{position:absolute;left:27.5px}
.nav-item.is-active{color:var(--orange)}
.nav-item.is-active::before{content:"";position:absolute;left:0;top:1px;width:2px;height:12px;background:var(--orange)}
.upload-btn{position:absolute;left:0;top:386px;width:91px;height:26px;background:var(--orange);color:var(--white);border-radius:0 13px 13px 0;font-size:6.7px;font-weight:700;display:flex;align-items:center;justify-content:center}
.topbar{position:absolute;top:0;left:0;width:100%;height:40px}
.top-icon{position:absolute;top:9.5px;width:17px;height:17px;border-radius:50%;background:var(--white);display:flex;align-items:center;justify-content:center;box-shadow:0 1px 3px rgba(0,0,0,.06)}
.practice,.welcome{position:absolute;top:13px;font-size:6.9px;color:var(--ink)}
.practice{left:318px}
.welcome{left:435.5px}
.avatar{position:absolute;left:405px;top:7px;width:21px;height:21px;border-radius:50%;background:linear-gradient(#c9b7a6,#6d6a68)}
.avatar-status{position:absolute;left:422px;top:23.5px;width:4px;height:4px;border-radius:50%;background:#6fd23a}
.logout{position:absolute;left:498px;top:9px;width:18px;height:18px;border-radius:50%;background:var(--ink);display:flex;align-items:center;justify-content:center}
.card{position:absolute;left:92px;width:433.5px;background:var(--white);border-radius:9px;box-shadow:0 4px 14px rgba(30,80,110,.08)}
.card--session{top:89.4px;height:212px}
.card--library{top:82px;height:270.6px}
.patient-name{position:absolute;left:0;width:100%;top:40px;text-align:center;font-size:27px;font-weight:700;font-style:italic;color:var(--ink)}
.select{position:absolute;top:89.6px;width:128px;height:26.6px;background:var(--field);border-radius:6px;box-shadow:0 3px 6px rgba(0,0,0,.06);font-size:5.2px;color:var(--muted);display:flex;align-items:center;padding-left:8px}
.select::after{content:"";position:absolute;right:7px;top:12px;border-left:2.2px solid transparent;border-right:2.2px solid transparent;border-top:2.5px solid #444}
.btn{position:absolute;background:var(--orange);color:var(--white);border-radius:13px;display:flex;align-items:center;justify-content:center;font-weight:700;box-shadow:0 4px 8px rgba(249,157,28,.25)}
.btn--submit{left:166.5px;top:142px;width:99px;height:24px;font-size:7px}
.page-code{position:absolute;left:524px;top:414px;font-size:4.8px;color:#333}
.category-tabs{position:absolute;top:37px;left:0;width:100%;display:flex;justify-content:center;gap:7px;font-size:7.5px;color:var(--text)}
.category-tabs .sep{color:#666}
.category-tabs .is-current{color:var(--orange)}
.form-card{position:absolute;width:124px;height:158px;background:var(--white);border-radius:8px;box-shadow:0 4px 14px rgba(30,80,110,.10);text-align:center}
.form-icon{position:absolute;left:43.4px;top:10.4px;width:37.2px;height:37.2px;border-radius:50%;background:var(--ink);display:flex;align-items:center;justify-content:center}
.form-title{position:absolute;top:53px;left:0;width:100%;font-size:9.5px;font-weight:700;color:var(--ink)}
.form-desc{position:absolute;top:69.5px;left:6px;right:6px;font-size:6.1px;line-height:12.8px;color:var(--text)}
.btn--learn{left:19.5px;top:126px;width:85px;height:21px;font-size:7px;border-radius:11px}
</style>
</head>
<body>

<!-- Session screen -->
<section class="screen screen--session">
  <aside class="sidebar">
    <svg class="menu-toggle" width="8" height="7" viewBox="0 0 8 7"><rect width="8" height="1.3" fill="#fff"/><rect y="2.85" width="8" height="1.3" fill="#fff"/><rect y="5.7" width="8" height="1.3" fill="#fff"/></svg>
    <ul class="nav">
      <li class="nav-item is-active" style="top:51px"><svg viewBox="0 0 8 8"><path d="M4 .5 .3 4h1.2v3.5h2V5.3h1v2.2h2V4h1.2z" fill="currentColor"/></svg><span>HOME</span></li>
      <li class="nav-item" style="top:80.3px"><svg viewBox="0 0 8 8"><rect x="1" y="1.5" width="6" height="6" fill="currentColor"/></svg><span>SCHEDULER</span></li>
      <li class="nav-item" style="top:109.6px"><svg viewBox="0 0 8 8"><circle cx="4" cy="2.3" r="1.8" fill="currentColor"/><path d="M1 7.7c0-2 1.3-3.2 3-3.2s3 1.2 3 3.2z" fill="currentColor"/></svg><span>PATIENTS</span></li>
      <li class="nav-item" style="top:138.9px"><svg viewBox="0 0 8 8"><path d="M1.5.3h3.5l2 2v5.4h-5.5z" fill="currentColor"/></svg><span>ENCOUNTERS</span></li>
      <li class="nav-item" style="top:168.2px"><svg viewBox="0 0 8 8"><text x="1.5" y="7.5" font-size="9" font-family="Lato,sans-serif" font-weight="700" fill="currentColor">$</text></svg><span>PAYMENTS</span></li>
      <li class="nav-item" style="top:197.5px"><svg viewBox="0 0 8 8"><path d="M1.5.3h3.5l2 2v5.4h-5.5z" fill="currentColor"/></svg><span>BILLING</span></li>
      <li class="nav-item" style="top:226.8px"><svg viewBox="0 0 8 8"><path d="M.5 1v6.5h7" stroke="currentColor" fill="none"/><path d="M1.5 6 3.5 3.5 5 5 7 2" stroke="currentColor" fill="none"/></svg><span>REPORT</span></li>
      <li class="nav-item" style="top:256.1px"><svg viewBox="0 0 8 8"><circle cx="4" cy="4" r="3.4" stroke="currentColor" fill="none" stroke-width=".8"/><circle cx="4" cy="4" r="1.8" stroke="currentColor" fill="none" stroke-width=".8"/><circle cx="4" cy="4" r=".6" fill="currentColor"/></svg><span>MARKETING</span></li>
      <li class="nav-item" style="top:285.4px"><svg viewBox="0 0 8 8"><path d="M1.5.3h3.5l2 2v5.4h-5.5z" fill="currentColor"/></svg><span>FORMS</span></li>
      <li class="nav-item" style="top:314.7px"><svg viewBox="0 0 8 8"><g fill="currentColor"><rect x=".5" y="1" width="1.3" height="1.3"/><rect x=".5" y="3.4" width="1.3" height="1.3"/><rect x=".5" y="5.8" width="1.3" height="1.3"/><rect x="2.6" y="1.2" width="5" height=".9"/><rect x="2.6" y="3.6" width="5" height=".9"/><rect x="2.6" y="6" width="5" height=".9"/></g></svg><span>LISTS</span></li>
      <li class="nav-item" style="top:344px"><svg viewBox="0 0 8 8"><g fill="currentColor"><circle cx="2" cy="3" r="1.2"/><circle cx="4.6" cy="2.4" r="1.5"/><path d="M0 7c0-1.6.9-2.5 2-2.5S4 5.4 4 7zM2.3 7.5c0-2 1-3.3 2.3-3.3S7 5.5 7 7.5z"/></g></svg><span>ADMIN</span></li>
    </ul>
    <div class="upload-btn">Upload additional forms</div>
  </aside>

  <header class="topbar">
    <div class="top-icon" style="left:244.5px"><svg width="8" height="8" viewBox="0 0 8 8"><path d="M4 1c-1.5 0-2.4 1-2.4 2.4v1.6L.9 6h6.2l-.7-1V3.4C6.4 2 5.5 1 4 1zM3.2 6.7h1.6a.8.8 0 0 1-1.6 0z" fill="none" stroke="#f99d1c" stroke-width=".7"/></svg></div>
    <div class="top-icon" style="left:269px"><svg width="8" height="8" viewBox="0 0 8 8"><path d="M7.4.6 .6 3.6 3 4.6 4 7.4z M3 4.6 7.4.6" fill="none" stroke="#f99d1c" stroke-width=".7"/></svg></div>
    <div class="top-icon" style="left:292.5px"><svg width="8" height="8" viewBox="0 0 8 8"><rect x="1.5" y="1.5" width="5" height="6" fill="#f99d1c"/><rect x="3" y=".5" width="2" height="1.3" fill="#f99d1c"/><g fill="#fff"><rect x="2.4" y="3" width="1" height="1"/><rect x="4.6" y="3" width="1" height="1"/><rect x="3.5" y="5.5" width="1" height="2"/></g></svg></div>
    <div class="practice">Sample Healthcare Practice</div>
    <div class="avatar" role="img" aria-label="User profile photo"></div>
    <div class="avatar-status"></div>
    <div class="welcome">Welcome Back,Test</div>
    <div class="logout"><svg width="8" height="8" viewBox="0 0 8 8"><path d="M3 1H1v6h2" stroke="#fff" fill="none" stroke-width=".9"/><path d="M3 3h2.5V1.6L7.7 4 5.5 6.4V5H3z" fill="#fff"/></svg></div>
  </header>

  <div class="card card--session">
    <h1 class="patient-name">Alan Moss</h1>
    <div class="select" style="left:17px">Selected Date</div>
    <div class="select" style="left:153px">Selected Provider</div>
    <div class="select" style="left:288.6px">Selected Author</div>
    <div class="btn btn--submit">SUBMIT</div>
  </div>
  <div class="page-code">C 43</div>
</section>

<!-- Forms library screen -->
<section class="screen screen--forms">
  <aside class="sidebar">
    <svg class="menu-toggle" width="8" height="7" viewBox="0 0 8 7"><rect width="8" height="1.3" fill="#fff"/><rect y="2.85" width="8" height="1.3" fill="#fff"/><rect y="5.7" width="8" height="1.3" fill="#fff"/></svg>
    <ul class="nav">
      <li class="nav-item" style="top:51px"><svg viewBox="0 0 8 8"><path d="M4 .5 .3 4h1.2v3.5h2V5.3h1v2.2h2V4h1.2z" fill="currentColor"/></svg><span>HOME</span></li>
      <li class="nav-item" style="top:80.3px"><svg viewBox="0 0 8 8"><rect x="1" y="1.5" width="6" height="6" fill="currentColor"/></svg><span>SCHEDULER</span></li>
      <li class="nav-item" style="top:109.6px"><svg viewBox="0 0 8 8"><circle cx="4" cy="2.3" r="1.8" fill="currentColor"/><path d="M1 7.7c0-2 1.3-3.2 3-3.2s3 1.2 3 3.2z" fill="currentColor"/></svg><span>PATIENTS</span></li>
      <li class="nav-item" style="top:138.9px"><svg viewBox="0 0 8 8"><path d="M1.5.3h3.5l2 2v5.4h-5.5z" fill="currentColor"/></svg><span>ENCOUNTERS</span></li>
      <li class="nav-item" style="top:168.2px"><svg viewBox="0 0 8 8"><text x="1.5" y="7.5" font-size="9" font-family="Lato,sans-serif" font-weight="700" fill="currentColor">$</text></svg><span>PAYMENTS</span></li>
      <li class="nav-item" style="top:197.5px"><svg viewBox="0 0 8 8"><path d="M1.5.3h3.5l2 2v5.4h-5.5z" fill="currentColor"/></svg><span>BILLING</span></li>
      <li class="nav-item" style="top:226.8px"><svg viewBox="0 0 8 8"><path d="M.5 1v6.5h7" stroke="currentColor" fill="none"/><path d="M1.5 6 3.5 3.5 5 5 7 2" stroke="currentColor" fill="none"/></svg><span>REPORT</span></li>
      <li class="nav-item" style="top:256.1px"><svg viewBox="0 0 8 8"><circle cx="4" cy="4" r="3.4" stroke="currentColor" fill="none" stroke-width=".8"/><circle cx="4" cy="4" r="1.8" stroke="currentColor" fill="none" stroke-width=".8"/><circle cx="4" cy="4" r=".6" fill="currentColor"/></svg><span>MARKETING</span></li>
      <li class="nav-item is-active" style="top:285.4px"><svg viewBox="0 0 8 8"><path d="M1.5.3h3.5l2 2v5.4h-5.5z" fill="currentColor"/></svg><span>FORMS</span></li>
      <li class="nav-item" style="top:314.7px"><svg viewBox="0 0 8 8"><g fill="currentColor"><rect x=".5" y="1" width="1.3" height="1.3"/><rect x=".5" y="3.4" width="1.3" height="1.3"/><rect x=".5" y="5.8" width="1.3" height="1.3"/><rect x="2.6" y="1.2" width="5" height=".9"/><rect x="2.6" y="3.6" width="5" height=".9"/><rect x="2.6" y="6" width="5" height=".9"/></g></svg><span>LISTS</span></li>
      <li class="nav-item" style="top:344px"><svg viewBox="0 0 8 8"><g fill="currentColor"><circle cx="2" cy="3" r="1.2"/><circle cx="4.6" cy="2.4" r="1.5"/><path d="M0 7c0-1.6.9-2.5 2-2.5S4 5.4 4 7zM2.3 7.5c0-2 1-3.3 2.3-3.3S7 5.5 7 7.5z"/></g></svg><span>ADMIN</span></li>
    </ul>
    <div class="upload-btn">Upload additional forms</div>
  </aside>

  <header class="topbar">
    <div class="top-icon" style="left:244.5px"><svg width="8" height="8" viewBox="0 0 8 8"><path d="M4 1c-1.5 0-2.4 1-2.4 2.4v1.6L.9 6h6.2l-.7-1V3.4C6.4 2 5.5 1 4 1zM3.2 6.7h1.6a.8.8 0 0 1-1.6 0z" fill="none" stroke="#f99d1c" stroke-width=".7"/></svg></div>
    <div class="top-icon" style="left:269px"><svg width="8" height="8" viewBox="0 0 8 8"><path d="M7.4.6 .6 3.6 3 4.6 4 7.4z M3 4.6 7.4.6" fill="none" stroke="#f99d1c" stroke-width=".7"/></svg></div>
    <div class="top-icon" style="left:292.5px"><svg width="8" height="8" viewBox="0 0 8 8"><rect x="1.5" y="1.5" width="5" height="6" fill="#f99d1c"/><rect x="3" y=".5" width="2" height="1.3" fill="#f99d1c"/><g fill="#fff"><rect x="2.4" y="3" width="1" height="1"/><rect x="4.6" y="3" width="1" height="1"/><rect x="3.5" y="5.5" width="1" height="2"/></g></svg></div>
    <div class="practice">Sample Healthcare Practice</div>
    <div class="avatar" role="img" aria-label="User profile photo"></div>
    <div class="avatar-status"></div>
    <div class="welcome">Welcome Back,Test</div>
    <div class="logout"><svg width="8" height="8" viewBox="0 0 8 8"><path d="M3 1H1v6h2" stroke="#fff" fill="none" stroke-width=".9"/><path d="M3 3h2.5V1.6L7.7 4 5.5 6.4V5H3z" fill="#fff"/></svg></div>
  </header>

  <div class="card card--library">
    <nav class="category-tabs">
      <span class="is-current">OFFICE</span><span class="sep">|</span>
      <span>SCHEDULER</span><span class="sep">|</span>
      <span>PATIENT</span><span class="sep">|</span>
      <span>RELEASE</span><span class="sep">|</span>
      <span>CERTIFICATES</span><span class="sep">|</span>
      <span>INSURANCE</span><span class="sep">|</span>
      <span>OTHER</span>
    </nav>
  </div>

  <article class="form-card" style="left:109px;top:155px">
    <div class="form-icon"><svg width="20" height="20" viewBox="0 0 20 20" fill="none" stroke="#fff" stroke-width=".9"><path d="M4 6 2.5 15l7 2"/><path d="M6 4v12h9V6l-2-2z"/><path d="M8 7h5M8 9h5M8 11h5M8 13h4"/></svg></div>
    <h2 class="form-title">LETTERHEAD</h2>
    <p class="form-desc">Lorem ipsum dolor sit amet, consectetur adipiscing elit, sed do eiusmod tempor incididunt ut labore et dolore magna aliqua.</p>
    <div class="btn btn--learn">LEARN MORE</div>
  </article>

  <article class="form-card" style="left:246.5px;top:140px">
    <div class="form-icon"><svg width="20" height="20" viewBox="0 0 20 20" fill="none" stroke="#fff" stroke-width=".9"><path d="M4 3h10v14H4z"/><path d="M6 6h6M6 8h6M6 10h4M6 12h3"/><path d="M10 15l1-3 5-5 2 2-5 5z"/></svg></div>
    <h2 class="form-title">SIGN-IN SHEET</h2>
    <p class="form-desc">Lorem ipsum dolor sit amet, consectetur adipiscing elit, sed do eiusmod tempor incididunt ut labore et dolore magna aliqua.</p>
    <div class="btn btn--learn">LEARN MORE</div>
  </article>

  <article class="form-card" style="left:384px;top:155px">
    <div class="form-icon"><svg width="20" height="20" viewBox="0 0 20 20" fill="none" stroke="#fff" stroke-width=".9"><path d="M7 3h6v5H7z"/><path d="M3 8h14v9H3z"/><path d="M5 9v7"/><path d="M9 10h6v2H9z"/><path d="M9 13.5h1.2M11.5 13.5h1.2M14 13.5h1M9 15.5h1.2M11.5 15.5h1.2M14 15.5h1"/></svg></div>
    <h2 class="form-title">FAX COVER SHEET</h2>
    <p class="form-desc">Lorem ipsum dolor sit amet, consectetur adipiscing elit, sed do eiusmod tempor incididunt ut labore et dolore magna aliqua.</p>
    <div class="btn btn--learn">LEARN MORE</div>
  </article>

  <div class="page-code">C 43</div>
</section>

</body>
</html>
```